Edit of business card / magnet

Hi there
Can you please edit the attached business card which I am going to use to print on a magnet. Can you please edit the following:
1) Make it 54 x 90mm with a 3 mm bleed.
2) I need 3 different versions. Each version will be the same with the exception of the following sentence which I need added underneath the Pinecrest Plumbing Services Pty Limited logo:
i) Your local Cherrybrook plumber
ii) Your local Wahroonga plumber
iii) Your local St Ives plumber
3) Can you add the wording "Present this card to receive a $50 discount" somewhere
4) On the right hand side where it lists the different types of services can you add a point "we can work within your budget"
Thanks

```html
<!DOCTYPE html>
<html lang="en">
<head>
<meta charset="utf-8">
<title>Pinecrest Plumbing – Business Card</title>
<link rel="stylesheet" href="https://fonts.googleapis.com/css2?family=Cabin:wght@400;500;700&display=swap">
<style>
  :root {
    --brand-blue: #1274c9;
    --panel-blue: #1a82d4;
    --panel-glow: rgba(255, 255, 255, 0.22);
    --pipe-grey: #8c8f93;
    --ink: #141414;
    --paper: #ffffff;
    --stage: #e6e7e9;
  }
  * { box-sizing: border-box; margin: 0; padding: 0; }
  html, body {
    width: 1200px;
    height: 800px;
    overflow: hidden;
    background: var(--stage);
    font-family: "Cabin", sans-serif;
  }
  .card {
    position: absolute;
    left: 150px;
    top: 130px;
    width: 900px;
    height: 540px;
    background: var(--paper);
    overflow: hidden;
    box-shadow: 0 10px 30px rgba(0, 0, 0, 0.18);
  }
  .services-panel {
    position: absolute;
    left: 430px;
    top: 0;
    width: 470px;
    height: 540px;
    background: var(--panel-blue);
  }
  .panel-glow {
    position: absolute;
    left: -60px;
    top: 120px;
    width: 300px;
    height: 340px;
    border-radius: 50%;
    background: radial-gradient(ellipse at 55% 45%, var(--panel-glow), rgba(255,255,255,0) 70%);
  }
  .brand {
    position: absolute;
    left: 60px;
    top: 70px;
    width: 330px;
  }
  .brand-mark {
    width: 54px;
    height: 54px;
    border-radius: 50%;
    background: var(--brand-blue);
    margin: 0 0 18px 132px;
  }
  .brand-name {
    color: var(--brand-blue);
    font-weight: 700;
    font-size: 62px;
    line-height: 0.9;
    text-align: right;
    letter-spacing: -1px;
  }
  .brand-entity {
    color: var(--pipe-grey);
    font-size: 21px;
    letter-spacing: 0.5px;
    text-align: right;
    margin-top: 6px;
  }
  .tagline { margin-top: 20px; text-align: right; }
  .tagline-lead { display: block; color: var(--pipe-grey); font-size: 20px; text-align: left; padding-left: 40px; }
  .tagline-suburb { display: block; color: var(--brand-blue); font-weight: 700; font-size: 44px; line-height: 1; }
  .tagline-trail { display: block; color: var(--pipe-grey); font-size: 17px; }
  .services {
    position: absolute;
    right: 40px;
    top: 56px;
    text-align: right;
    color: var(--paper);
    list-style: none;
    font-size: 29px;
    line-height: 36px;
    text-transform: uppercase;
  }
  .budget {
    position: absolute;
    right: 40px;
    top: 270px;
    text-align: right;
    color: var(--paper);
    font-size: 29px;
    line-height: 34px;
    text-transform: uppercase;
  }
  .contact {
    position: absolute;
    right: 40px;
    top: 360px;
    text-align: right;
    color: var(--paper);
    font-style: normal;
  }
  .licence { font-size: 15px; opacity: 0.85; }
  .phone { font-size: 28px; font-weight: 500; letter-spacing: 1px; }
  .email, .web { font-size: 19px; line-height: 24px; }
  .offer {
    position: absolute;
    left: 24px;
    bottom: 18px;
    display: flex;
    align-items: center;
    gap: 16px;
  }
  .partner-badge {
    width: 28px;
    height: 24px;
    background: #d8b24a;
  }
  .offer-text {
    color: var(--ink);
    font-size: 17px;
    font-weight: 500;
    letter-spacing: 7px;
    text-transform: uppercase;
  }
</style>
</head>
<body>
  <main class="card">
    <section class="services-panel">
      <div class="panel-glow"></div>
      <ul class="services">
        <li>Plumbing Services</li>
        <li>Hot Water Systems</li>
        <li>Gas Services</li>
        <li>Blocked Drains</li>
        <li>Taps Toilets</li>
      </ul>
      <p class="budget">We can work<br>within your budget</p>
      <address class="contact">
        <div class="licence">Lic #100238c</div>
        <div class="phone">0400 555 018</div>
        <div class="email">enquiry@pinecrestplumbing.com.au</div>
        <div class="web">www.pinecrestplumbing.com.au</div>
      </address>
    </section>

    <header class="brand">
      <div class="brand-mark"></div>
      <h1 class="brand-name">Pinecrest<br>Plumbing</h1>
      <p class="brand-entity">SERVICES PTY LTD</p>
      <p class="tagline">
        <span class="tagline-lead">Your local</span>
        <span class="tagline-suburb">Cherrybrook</span>
        <span class="tagline-trail">plumber.</span>
      </p>
    </header>

    <footer class="offer">
      <div class="partner-badge" aria-hidden="true"></div>
      <p class="offer-text">Present this card to receive a $50 discount.</p>
    </footer>
  </main>
</body>
</html>
```